TitleForge.com - Brandable Business Name Marketplace!

What is Title Forge?
Title Forge is a website that helps businesses build a name (or find a new name) for
their new product, service, or business. Over 2 million new businesses start each year,
and even more new products are created, and each one needs a unique name!
Other competitor branding sites for reference: www.MarkPail.com, www.Tagtastic.com, www.SignStem.com, www.markzo.com
What does Title Forge do?
Every business/product has a website, and the ‘address’ of the website is called
a ‘domain name’. We find valuable ‘domain names’ that are unique, catchy, or keyword-rich.
We then create a logo to capture the vision of the possibilities of that name. Then we write a
creative description of name, which further evolves the vision of the name.
We also help domain owners submit and sell their valuable digital real estate (domain).
How does the website function?
The ‘home’ page of the site should be modern, clean, and straight to the point (the
logos). The main focus is on the ‘logos’. There should be 5-6 logos per row and around
100 logos per page. The ‘description’ of each logo is NOT displayed UNTIL the visitor
clicks on a logo. Then the description, tags, category, and price will EXPAND ON SAME
PAGE (Not open in new page). Once the logo expands to reveal the description, tags,
category, and price, then the visitor can click on the name of the logo and THEN a
new page will open with options to add to cart or buy now.
What comes with each purchase?
1) Years of experience and expertise, ready to help builder your name!
2) Ownership of the valuable domain name, (digital real estate)
3) Custom logo artwork is included. And ideas for branding!
What happens after the customer completes purchase?
After completing our secure SSL checkout process, which accepts all major credit
cards and options for bank wire. The customer will be emailed transfer instructions.
The payment is held in escrow until the customer confirms delivery of the domain name.
Does title forge own all the names on the site?
Not all the names, some. Title forge allows owners of domain names to
‘Submit’ their domain names for acceptance to be listed on our site. After our team ‘reviews’
the names, they will be accepted or rejected. The domain names that are suitable
for our target audience, will be emailed with instructions to ‘forward’ the domain to
the Title Forge site. Once our system verifies the domain is correctly forwarded, the
domain owner will be emailed with instructions and listing fees to be paid.
What the site needs:
1) The site must have a login for domain owners. Each domain owner will have
an account profile where they can:
• a) submit their domain names to list on our site
• b) verify accepted names
• c) pay listing fees
• d) describe what the domain means to the owner
• e) adjust the price (we determine fair market value) by 20% up or down.
• f) profile page (portfolio of names)
2) The site must display the logo artwork as the main focus of the site.
3) The site must have a newsletter page.
4) The site must have an about us page.
5) The site must have contact page.
6) The site must have a FAQ page.
7) The site must have a ‘search bar’
8) The site must have a ’price range filter’ to sort names.
9) The site must have an option to sort names by: categories
10) The site must have an option to ‘rearrange’ the logos by:
• a) ’Date’
• b) ’Price’
• c) ’Alphabetical order’
• d) ’Staff picks’.
Summary:
We want to help businesses build a name for their product/service/company. The true value of what we sell is in the domain names, however the inspiration, possibilities, and vision is captured in the logos. The site will get tons of natural traffic because all the domain names listed on the site will be forwarded to TitleForge.com and we will actively advertise. Upon arrival the visitors will see catchy, unique, and keyword rich logos. Upon clicking on a logo, the logo will expand to display, description, category, price, and possible business uses. Upon clicking further, a new page will open (the landing page for each domain name if entered directly into browser) which will give options to inquire, add to cart, favorite, or buy now!. There will be a login for domain owners where they can submit new domain names, verify ownership by forwarding domain, pay listing fee, describe accepted name, and adjust our chosen price up or down by 20%. They will also have a profile page which will display only their portfolio of names with logos. There will be a Newsletter, FAQ, About Us, Contact, and Login Pages.
Target Market(s)
Business owners who want a brandable name for their business/service/product
Industry/Entity Type
Business
Number of Pages Required
1 page
Look and feel

```html
<!DOCTYPE html>
<html lang="en">
<head>
<meta charset="utf-8">
<title>Title Forge – Brandable Business Names</title>
<link rel="stylesheet" href="https://fonts.googleapis.com/css2?family=Raleway:wght@400;500;600;700;800&display=swap">
<style>
:root{
  --ink:#ffffff;
  --space-deep:#05070f;
  --space-mid:#0b1430;
  --accent:#2b7ccc;
  --accent-dark:#1c5fa3;
  --card:#ffffff;
  --card-label:#cdd9e5;
  --tag:#d6dbe0;
  --tag-text:#3a3f46;
  --label-text:#34404d;
  --wordmark:#2b3340;
  --box-fill:rgba(10,12,20,.82);
}
*{box-sizing:border-box;margin:0;padding:0}
html,body{width:731px;height:1200px;overflow:hidden;background:var(--space-deep)}
body{position:relative;font-family:"Raleway",sans-serif;color:var(--ink)}

.backdrop{position:absolute;inset:0;
  background:
    radial-gradient(ellipse 260px 150px at 120px 150px,rgba(90,42,143,.75),transparent 70%),
    radial-gradient(ellipse 300px 160px at 420px 230px,rgba(31,79,156,.7),transparent 70%),
    radial-gradient(ellipse 220px 120px at 610px 120px,rgba(28,143,176,.45),transparent 70%),
    radial-gradient(ellipse 500px 120px at 365px 1215px,rgba(60,130,200,.55),transparent 70%),
    radial-gradient(ellipse 420px 80px at 365px 1205px,rgba(20,40,70,.9),transparent 80%),
    linear-gradient(180deg,var(--space-mid) 0%,#17174a 22%,#0b0f24 36%,var(--space-deep) 55%,#060a14 100%);}

/* navigation */
.nav{position:absolute;top:30px;left:127px;width:475px;height:24px;border-bottom:1px solid rgba(255,255,255,.55)}
.nav a{position:absolute;top:3px;font-size:9px;font-weight:500;color:var(--ink);text-decoration:none;white-space:nowrap}
.nav a.active{border-bottom:1px solid var(--ink)}
.nav .login{top:0;left:277px;width:45px;height:16px;border-radius:8px;background:var(--accent);text-align:center;line-height:16px}
.search{position:absolute;left:331px;top:0;width:98px;height:16px;border:1.5px solid var(--ink);border-radius:8px;font-size:7.5px;line-height:13px;padding-left:8px}
.search svg{position:absolute;right:7px;top:2px}
.cart{position:absolute;left:437px;top:-1px}
.cart-count{position:absolute;left:458px;top:1px;width:14px;height:14px;border-radius:50%;background:var(--ink);color:#1a1a2a;font-size:8px;font-weight:700;text-align:center;line-height:14px}

/* brand */
.brand-mark{position:absolute;left:343px;top:126px;width:44px;height:44px;border:3px solid var(--ink);border-radius:50%}
.brand-name{position:absolute;top:180px;left:0;width:731px;text-align:center;font-size:26px;font-weight:700;letter-spacing:.3px}

/* filters */
.filters{position:absolute;top:270px;left:0;width:731px;height:17px}
.pill{position:absolute;height:17px;border-radius:9px;font-size:8px;font-weight:600;text-align:center;line-height:15px;border:1.5px solid var(--ink)}
.pill.solid{background:var(--accent);border-color:var(--accent)}
.price-range{position:absolute;left:372px;width:132px;height:17px;border-radius:9px;background:var(--accent-dark);font-size:8px;font-weight:600;line-height:17px}
.price-range span{position:absolute;top:0}
.price-range .mid{left:30px;width:62px;height:17px;background:var(--accent);text-align:center}

.social{position:absolute;top:304px;left:325px;display:flex;gap:4px}
.social i{display:block;width:13px;height:13px;border-radius:50%;background:var(--ink)}

/* collections */
.collection{position:absolute;top:395px;width:185px;height:61px;border:2px solid var(--ink);background:var(--box-fill);font-size:16.5px;font-weight:600;text-align:center;line-height:57px;letter-spacing:.2px}

.section-title{position:absolute;top:507px;width:731px;text-align:center;font-size:13px;font-weight:700}
.section-sub{position:absolute;top:537px;width:731px;text-align:center;font-size:8.5px;font-weight:600}

/* grid */
.grid{position:absolute;top:578px;left:57px;display:grid;grid-template-columns:repeat(6,95px);grid-auto-rows:97px;column-gap:9px;row-gap:18px}
.card{position:relative;background:var(--card);box-shadow:0 2px 6px rgba(0,0,0,.5)}
.price-tag{position:absolute;top:-6px;left:25px;width:45px;height:14px;background:var(--tag);color:var(--tag-text);font-size:7.5px;font-weight:600;text-align:center;line-height:14px}
.mark{height:70px;display:flex;align-items:center;justify-content:center;font-size:14px;font-weight:600;color:var(--wordmark);padding-top:6px;white-space:nowrap}
.domain{height:27px;background:var(--card-label);color:var(--label-text);font-size:8px;font-weight:500;text-align:center;line-height:27px}
.card.selected .price-tag{background:var(--accent);color:var(--ink)}
.card.selected .domain{background:var(--accent);color:var(--ink)}

/* pagination */
.pager{position:absolute;top:1040px;left:235px;width:261px;height:21px;border-radius:3px;background:var(--accent);display:flex;align-items:center;gap:5px;padding:0 10px;font-size:7px;font-weight:700}
.pager i{display:block;width:10px;height:10px;border-radius:50%;background:var(--ink)}
.pager .arrow{font-size:10px;font-style:normal}
.pager .num{margin:0 3px}
.pager .oval{width:14px;border-radius:5px}

/* footer */
.payments{position:absolute;top:1127px;left:113px;display:flex;gap:4px}
.payments i{display:block;width:21px;height:14px;border-radius:2px;background:#e9edf2}
.phone{position:absolute;top:1128px;left:220px;font-size:9px;font-weight:600}
.legal{position:absolute;top:1151px;left:88px;font-size:8.5px;font-weight:500}
.legal u{color:#7fb6ea}
.cta{position:absolute;top:1123px;left:488px;width:68px;height:23px;border:1.5px solid var(--ink);background:var(--box-fill);font-size:8px;font-weight:700;text-align:center;line-height:20px}
.bubble{position:absolute;top:1089px;left:564px;width:70px;height:66px;border:1.5px solid var(--ink);border-radius:50%;background:var(--box-fill);font-size:8px;font-weight:600;text-align:center;line-height:11px;padding-top:17px}
.bubble-dot{position:absolute;border:1.5px solid var(--ink);border-radius:50%;background:var(--box-fill)}
</style>
</head>
<body>
<div class="backdrop" role="img" aria-label="Starry deep-space nebula in violet and blue with faint cloud-shaped name badges, fading to a dark sky above the glowing curve of the Earth at night"></div>

<nav class="nav">
  <a class="active" style="left:2px">Home</a>
  <a style="left:44px">Shop</a>
  <a style="left:86px">About Us</a>
  <a style="left:139px">Help</a>
  <a style="left:178px">Cart</a>
  <a style="left:214px">News Letter</a>
  <a class="login">Login</a>
  <div class="search">Search
    <svg width="8" height="8" viewBox="0 0 8 8"><circle cx="3.3" cy="3.3" r="2.4" fill="none" stroke="#fff" stroke-width="1.2"/><line x1="5" y1="5" x2="7.5" y2="7.5" stroke="#fff" stroke-width="1.2"/></svg>
  </div>
  <svg class="cart" width="18" height="15" viewBox="0 0 18 15"><path d="M1 2h3l2 8h9l2-6H5" fill="none" stroke="#fff" stroke-width="1.5"/><circle cx="7" cy="13" r="1.4" fill="#fff"/><circle cx="14" cy="13" r="1.4" fill="#fff"/></svg>
  <span class="cart-count">0</span>
</nav>

<div class="brand-mark"></div>
<h1 class="brand-name">Title Forge</h1>

<div class="filters">
  <div class="pill" style="left:227px;width:76px">Category</div>
  <div class="pill solid" style="left:307px;width:56px">Sort By</div>
  <div class="price-range"><span style="left:12px">$</span><span class="mid">Filter Price</span><span style="left:114px">$</span></div>
</div>
<div class="social"><i></i><i></i><i></i><i></i><i></i></div>

<div class="collection" style="left:63px">INVENTED NAMES</div>
<div class="collection" style="left:273px">KEYWORD NAMES</div>
<div class="collection" style="left:483px">NEW EXTENSIONS</div>

<h2 class="section-title">FEATURED NAMES</h2>
<p class="section-sub">NEWLY LISTED &nbsp;•&nbsp; STAFF PICKS</p>

<main class="grid">
  <div class="card selected"><span class="price-tag">$3,295</span><div class="mark">Robivo</div><div class="domain">robivo.com</div></div>
  <div class="card"><span class="price-tag">$3,295</span><div class="mark">DewCrate</div><div class="domain">dewcrate.com</div></div>
  <div class="card"><span class="price-tag">$3,295</span><div class="mark">Glowvra</div><div class="domain">glowvra.com</div></div>
  <div class="card"><span class="price-tag">$3,295</span><div class="mark">Guidenly</div><div class="domain">guidenly.com</div></div>
  <div class="card"><span class="price-tag">$3,295</span><div class="mark">Velora</div><div class="domain">velora.com</div></div>
  <div class="card"><span class="price-tag">$3,295</span><div class="mark">Nestbreeze</div><div class="domain">nestbreeze.com</div></div>

  <div class="card"><span class="price-tag">$3,295</span><div class="mark">Omtomo</div><div class="domain">omtomo.com</div></div>
  <div class="card"><span class="price-tag">$3,295</span><div class="mark">Blendora</div><div class="domain">blendora.com</div></div>
  <div class="card"><span class="price-tag">$3,295</span><div class="mark">Tunevo</div><div class="domain">tunevo.com</div></div>
  <div class="card"><span class="price-tag">$3,295</span><div class="mark">Tidora</div><div class="domain">tidora.com</div></div>
  <div class="card"><span class="price-tag">$3,295</span><div class="mark">Vigorix</div><div class="domain">vigorix.com</div></div>
  <div class="card"><span class="price-tag">$3,295</span><div class="mark">Pilecherry</div><div class="domain">pilecherry.com</div></div>

  <div class="card"><span class="price-tag">$3,295</span><div class="mark">Voltique</div><div class="domain">voltique.com</div></div>
  <div class="card"><span class="price-tag">$3,295</span><div class="mark">Shrinex</div><div class="domain">shrinex.com</div></div>
  <div class="card"><span class="price-tag">$3,295</span><div class="mark">Launchio</div><div class="domain">launchio.com</div></div>
  <div class="card"><span class="price-tag">$3,295</span><div class="mark">Humtronix</div><div class="domain">humtronix.com</div></div>
  <div class="card"><span class="price-tag">$3,295</span><div class="mark">Datumly</div><div class="domain">datumly.com</div></div>
  <div class="card"><span class="price-tag">$3,295</span><div class="mark">Fruvella</div><div class="domain">fruvella.com</div></div>

  <div class="card"><span class="price-tag">$3,295</span><div class="mark">Voltique</div><div class="domain">voltique.com</div></div>
  <div class="card"><span class="price-tag">$3,295</span><div class="mark">Shrinex</div><div class="domain">shrinex.com</div></div>
  <div class="card"><span class="price-tag">$3,295</span><div class="mark">Launchio</div><div class="domain">launchio.com</div></div>
  <div class="card"><span class="price-tag">$3,295</span><div class="mark">Humtronix</div><div class="domain">humtronix.com</div></div>
  <div class="card"><span class="price-tag">$3,295</span><div class="mark">Datumly</div><div class="domain">datumly.com</div></div>
  <div class="card"><span class="price-tag">$3,295</span><div class="mark">Fruvella</div><div class="domain">fruvella.com</div></div>
</main>

<div class="pager">
  <em class="arrow">‹</em>
  <span class="num">1</span>
  <i></i><i></i><i></i><i></i><i></i><i></i><i></i><i></i><i></i><i></i>
  <span class="num">100</span>
  <i class="oval"></i>
  <em class="arrow" style="margin-left:auto">›</em>
</div>

<footer>
  <div class="payments"><i></i><i></i><i></i><i></i></div>
  <div class="phone">1 - 800 - 000 - 0000</div>
  <p class="legal">© 2015 Title Forge . All Reserved / <u>TOS</u> / Privacy Policy</p>
  <div class="cta">CLICK HERE</div>
  <span class="bubble-dot" style="left:558px;top:1140px;width:6px;height:6px"></span>
  <span class="bubble-dot" style="left:563px;top:1131px;width:8px;height:8px"></span>
  <div class="bubble">Didn't find<br>the Name you<br>wanted</div>
</footer>
</body>
</html>
```